The graphic design project is to create a book cover and potentially an accompanying logo for a book called The Steady Compass: A Field Guide for Guiding Teams Through Shifting Ground. The title is a working title and may change slightly. The book presents 10 capabilities that organizational leaders should have to be able to lead in a world filled with uncertainties. The main themes are the following:• Leaders need to be clear and focused about the overall mission, but also need to make strategic decisions with a diversity of opinions and options.• Leaders must anticipate where they will need to adapt in implementing strategy.• Leaders need to create a culture that promotes trust and agility.• Leaders need to be vigilant and look for early indicators of change. Show intellectual curiosity.• Leaders should be willing to experiment and learn from the experiments.The book is designed as a handbook. This will be a self published business book.The below graphic provides what are the key concepts representing each letter of “COMPASSING”. The right-hand column provides key words / phrases associated with the concepts.

Target Market(s)

Mid to Senior level executives at global companies across industries.

Colors

Designer to choose colors to be used in the design.

Requirements
Must have
• No must haves.
Nice to have
• Wide open on the design.

```html
<!DOCTYPE html>
<html lang="en">
<head>
<meta charset="utf-8">
<title>The Steady Compass — Book Cover</title>
<link href="https://fonts.googleapis.com/css2?family=Bebas+Neue&family=Open+Sans:wght@400;600&display=swap" rel="stylesheet">
<style>
  :root {
    --page-bg: #d3ebf8;
    --cover-dark: #07090d;
    --wall-mid: #1b2330;
    --glow-blue: #9fc4f0;
    --glow-white: #f4f8ff;
    --text-white: #ffffff;
    --accent-orange: #f7960f;
  }
  html, body {
    margin: 0;
    width: 1200px;
    height: 1200px;
    overflow: hidden;
    background: var(--page-bg);
  }
  .book-cover {
    position: absolute;
    left: 232px;
    top: 47px;
    width: 750px;
    height: 1125px;
    overflow: hidden;
    background: var(--cover-dark);
  }
  .cover-art {
    position: absolute;
    inset: 0;
    background:
      radial-gradient(ellipse 230px 420px at 600px 700px, var(--glow-white) 0%, var(--glow-blue) 45%, rgba(60,90,140,0.35) 75%, rgba(0,0,0,0) 100%),
      linear-gradient(180deg, var(--cover-dark) 0%, var(--wall-mid) 55%, #2a3446 100%);
  }
  .subtitle {
    position: absolute;
    left: 0;
    width: 730px;
    top: 62px;
    margin: 0;
    text-align: center;
    font-family: "Open Sans", sans-serif;
    font-weight: 400;
    font-size: 24px;
    line-height: 29px;
    color: var(--text-white);
  }
  .title {
    margin: 0;
    font-family: "Bebas Neue", sans-serif;
    font-weight: 400;
  }
  .title span {
    position: absolute;
    line-height: 1;
    white-space: nowrap;
  }
  .title-the {
    left: 423px;
    top: 250px;
    font-size: 86px;
    color: var(--text-white);
  }
  .title-main {
    left: 130px;
    top: 320px;
    font-size: 152px;
    color: var(--text-white);
  }
  .title-accent {
    left: 160px;
    top: 462px;
    font-size: 142px;
    color: var(--accent-orange);
  }
  .author-name {
    position: absolute;
    left: 150px;
    top: 1000px;
    margin: 0;
    font-family: "Bebas Neue", sans-serif;
    font-weight: 400;
    font-size: 66px;
    line-height: 1;
    letter-spacing: 22px;
    color: var(--text-white);
    white-space: nowrap;
  }
</style>
</head>
<body>
  <main class="book-cover">
    <div class="cover-art" role="img" aria-label="Photograph: dark brick wall broken open to bright light, a businessman with a briefcase walking toward the opening"></div>
    <p class="subtitle">A Field Guide for Guiding Teams<br>Through Shifting Ground</p>
    <h1 class="title">
      <span class="title-the">THE</span>
      <span class="title-main">STEADY</span>
      <span class="title-accent">COMPASS</span>
    </h1>
    <p class="author-name">AUTHOR NAME</p>
  </main>
</body>
</html>
```